Uplift: Covid 19 (Poster)

We are looking to create a 11 by 17 inch 1 page poster.
-- Please Include NKR’s logo
-- Use the colors and font and mimic the feel of from Steady Step, Steady Breath Resource - Dementia Risk Reduction Flyers - Northern Council for Tribal Longevity (nkrcircle.org)
--> https://nkrcircle.org/resource-dementia-risk-reduction-flyers/
Moto needs to be included and it is: Protect Your Community. Protect Your Elders. Stay Vaccinated.
Include funding statement at the bottom of document - small print:
This project is supported by the Bureau for Illness Monitoring and Response of the U.S. Office of Wellness and Family Programs (OWFP) as part of a financial assistance award totaling $20,007,444 with 100 percent funded by BIMR/OWFP. The contents are those of the author(s) and do not necessarily represent the official views of, nor an endorsement, by BIMR/OWFP, or the U.S. Government.

```html
<!DOCTYPE html>
<html lang="en">
<head>
<meta charset="utf-8">
<title>Protect Your Community – Fight COVID-19 Poster</title>
<link rel="stylesheet" href="https://fonts.googleapis.com/css2?family=Archivo+Black&family=Work+Sans:wght@400;600;700&display=swap">
<style>
  :root {
    --stage: #a3a3a3;
    --paper: #ede3d1;
    --teal: #3e9690;
    --rust: #a84b38;
    --brown: #4e2a1a;
    --crimson: #8e1f2b;
    --band-a: #9bbfbc;
    --band-b: #d9cbb5;
    --frame: #fbfaf7;
    --heading: "Archivo Black", "Arial Black", sans-serif;
    --body: "Work Sans", Arial, sans-serif;
  }
  * { box-sizing: border-box; margin: 0; padding: 0; }
  html, body { width: 1200px; height: 1000px; overflow: hidden; }
  body { background: var(--stage); font-family: var(--body); position: relative; }

  .poster {
    position: absolute; left: 290px; top: 18px; width: 620px; height: 964px;
    background: var(--paper); box-shadow: 0 2px 8px rgba(0,0,0,.25);
  }
  .band {
    position: absolute; left: 0; width: 100%; height: 34px;
    background: linear-gradient(180deg, var(--band-a), var(--band-b));
  }
  .band--top { top: 0; }
  .band--bottom { bottom: 0; background: linear-gradient(0deg, var(--band-a), var(--band-b)); }

  .brand {
    position: absolute; top: 44px; left: 0; width: 100%;
    display: flex; justify-content: center; align-items: center; gap: 8px;
  }
  .brand__mark { width: 14px; height: 14px; border-radius: 50%; background: var(--teal); }
  .brand__name { font-family: var(--body); font-weight: 700; font-size: 13px; color: var(--teal); text-transform: uppercase; letter-spacing: .2px; }

  .headline { position: absolute; top: 104px; left: 0; width: 100%; text-align: center; font-family: var(--heading); line-height: .9; }
  .headline__top { display: block; color: var(--teal); font-size: 58px; }
  .headline__main { display: block; color: var(--rust); font-size: 70px; letter-spacing: -1px; }

  .motto { position: absolute; top: 220px; left: 0; width: 100%; text-align: center; font-family: var(--heading); color: var(--brown); font-size: 18.5px; }
  .callout { position: absolute; top: 252px; left: 0; width: 100%; text-align: center; font-family: var(--heading); color: var(--crimson); font-size: 32px; }
  .callout__diamond { display: inline-block; width: 14px; height: 14px; background: var(--crimson); transform: rotate(45deg); margin: 0 14px; vertical-align: 6px; }

  .intro { position: absolute; top: 307px; left: 33px; width: 565px; color: var(--brown); font-size: 14.5px; line-height: 1.3; }
  .facts { position: absolute; top: 358px; left: 33px; width: 349px; color: var(--brown); font-weight: 700; font-size: 13.4px; line-height: 1.3; text-align: justify; }
  .facts p { margin-bottom: 17px; }

  .symptoms { position: absolute; top: 551px; left: 35px; list-style: none; color: var(--brown); font-weight: 600; font-size: 14px; }
  .symptoms li { height: 25.2px; display: flex; align-items: center; gap: 9px; }
  .symptoms li::before { content: ""; width: 9px; height: 9px; background: var(--crimson); transform: rotate(45deg); flex: none; }

  .snapshot { position: absolute; background: var(--frame); padding: 9px 9px 20px; box-shadow: 0 2px 6px rgba(0,0,0,.25); }
  .snapshot--family { left: 394px; top: 378px; width: 204px; height: 222px; transform: rotate(3deg); }
  .snapshot--elders { left: 384px; top: 576px; width: 214px; height: 262px; transform: rotate(-4deg); }
  .snapshot__fill { width: 100%; height: 100%; }
  .snapshot--family .snapshot__fill { background: linear-gradient(180deg, #b9a89a 0%, #a4694c 45%, #8b3f2c 100%); }
  .snapshot--elders .snapshot__fill { background: linear-gradient(160deg, #3a2418 0%, #8a4a6e 45%, #a6342a 80%, #d46a2c 100%); }

  .funding { position: absolute; top: 860px; left: 33px; width: 550px; display: flex; gap: 22px; align-items: flex-start; }
  .funding__brand { display: flex; align-items: center; gap: 5px; font-family: var(--body); font-weight: 700; font-size: 22px; color: var(--teal); padding-top: 6px; }
  .funding__brand .brand__mark { width: 10px; height: 10px; }
  .funding__text { font-size: 9.4px; line-height: 1.22; color: var(--rust); }
</style>
</head>
<body>
  <main class="poster">
    <div class="band band--top" role="img" aria-label="Decorative chevron border"></div>

    <header class="brand">
      <span class="brand__mark"></span>
      <span class="brand__name">Northern Council for Tribal Longevity</span>
    </header>

    <h1 class="headline">
      <span class="headline__top">PROTECT YOUR</span>
      <span class="headline__main">COMMUNITY</span>
    </h1>
    <p class="motto">PROTECT YOUR ELDERS. STAY VACCINATED.</p>
    <p class="callout"><span class="callout__diamond"></span>FIGHT COVID-19!<span class="callout__diamond"></span></p>

    <p class="intro">American Indian and Alaska Native people have a higher risk of COVID-19 infection rate than other population in the United States.</p>

    <div class="facts">
      <p>&nbsp;•COVID-19 is a virus that spreads mainly when infected people cough, sneeze, or talk.</p>
      <p>&nbsp;•The best way to prevent yourself and others from COVID-19 is by staying up to date with vaccination boosters.</p>
      <p>COVID-19 symptoms may take 2 to 14 days to appear after exposure to the virus, and symptoms may include:2</p>
    </div>

    <ul class="symptoms">
      <li>Fever or chills</li>
      <li>Cough</li>
      <li>Shortness of breath or difficulty breathing</li>
      <li>Fatigue</li>
      <li>Muscle or body aches</li>
      <li>Headache</li>
      <li>New loss of taste or smell</li>
      <li>Sore throat</li>
      <li>Congestion or runny nose</li>
      <li>Nausea or vomiting</li>
      <li>Diarrhea</li>
    </ul>

    <figure class="snapshot snapshot--family">
      <div class="snapshot__fill" role="img" aria-label="Photo of an Indigenous family in traditional blankets seated outside an earthen hogan in the desert"></div>
    </figure>
    <figure class="snapshot snapshot--elders">
      <div class="snapshot__fill" role="img" aria-label="Photo of two Indigenous elder women in traditional dress and woven blankets"></div>
    </figure>

    <footer class="funding">
      <div class="funding__brand"><span class="brand__mark"></span>NKR</div>
      <p class="funding__text">This project is supported by the Bureau for Illness Monitoring and Response of the U.S. Office of Wellness and Family Programs (OWFP) as part of a financial assistance award totaling $20,007,444 with 100 percent funded by BIMR/OWFP. The contents are those of the author(s) and do not necessarily represent the official views of, nor an endorsement, by BIMR/OWFP, or the U.S. Government.</p>
    </footer>

    <div class="band band--bottom" role="img" aria-label="Decorative chevron border"></div>
  </main>
</body>
</html>
```